Harbor Compass - Book Cover

I need a book cover for my debut work, "Harbor Compass - Turning the Tide, One Step at a Time." While the website isn't complete, you can get a sense of what I am writing about by looking at my website, harborcompassbooks.org. The book is a leadership development book, but more of a personal change journey. The emphasis is on figuring out how to combine you work, social, and own self into an authentic package that not only resonates with others, but makes what you achieve more fulfilling.

I am attaching a copy of my logo so you can get a sense of what I like. I would prefer to not have the cover be photographic, but am open to suggestions. This will be a series of books so maintaining some sense of style will be important, and can garner future work.

Industry/Entity Type

Leadership

```html
<!DOCTYPE html>
<html lang="en">
<head>
<meta charset="utf-8">
<title>Harbor Compass – Book Cover</title>
<link href="https://fonts.googleapis.com/css2?family=Open+Sans:ital,wght@0,400;0,500;0,600;0,700;1,400&display=swap" rel="stylesheet">
<style>
  :root {
    --blue: #1f58ad;
    --paper: #ececec;
    --ink: #111111;
    --grey: #4a4a4a;
    --stage: #2b2a2e;
    --white: #ffffff;
    --edge: #cfcfcf;
  }
  html, body {
    margin: 0;
    padding: 0;
    width: 1200px;
    height: 911px;
    overflow: hidden;
    background: var(--stage);
    font-family: "Open Sans", Arial, sans-serif;
  }
  .canvas {
    position: relative;
    width: 1200px;
    height: 911px;
  }
  .book-wrap {
    position: absolute;
    left: 218px;
    top: 185px;
    display: flex;
    height: 540px;
  }
  .cover {
    position: relative;
    width: 360px;
    height: 540px;
    background: var(--paper);
    overflow: hidden;
  }
  .band-top {
    position: absolute;
    left: 0; right: 0; top: 0;
    height: 40px;
    background: var(--blue);
  }
  .rule {
    position: absolute;
    height: 2px;
    background: var(--ink);
  }
  .series .series-lead { color: var(--blue); }
  .series .series-tail { color: var(--grey); }

  /* Front cover */
  .front .series {
    position: absolute;
    top: 78px; left: 0; right: 0;
    margin: 0;
    text-align: center;
    font-size: 26px;
    font-weight: 500;
  }
  .front .rule-top { top: 124px; left: 64px; width: 232px; }
  .front .title {
    position: absolute;
    top: 150px; left: 0; right: 0;
    margin: 0;
    text-align: center;
    font-size: 38px;
    font-weight: 500;
    line-height: 50px;
    color: var(--ink);
  }
  .front .title .accent { color: var(--blue); }
  .front .title .soft { color: var(--grey); }
  .front .rule-bottom { top: 370px; left: 64px; width: 232px; }
  .front .band-quote {
    position: absolute;
    left: 0; right: 0; top: 398px;
    height: 82px;
    background: var(--blue);
    display: flex;
    align-items: center;
    justify-content: center;
  }
  .front .band-quote p {
    margin: 0;
    width: 270px;
    text-align: center;
    font-size: 9px;
    font-style: italic;
    line-height: 12px;
    color: var(--white);
  }
  .front .author {
    position: absolute;
    top: 496px; left: 0; right: 0;
    margin: 0;
    text-align: center;
    font-size: 19px;
    font-weight: 500;
    color: var(--ink);
  }

  /* Spine */
  .spine {
    position: relative;
    width: 44px;
    height: 540px;
    background: var(--white);
    border-left: 1px solid var(--edge);
    border-right: 1px solid var(--edge);
    box-sizing: border-box;
  }
  .spine .spine-title {
    position: absolute;
    top: 24px;
    left: 50%;
    transform: translateX(-50%);
    writing-mode: vertical-rl;
    margin: 0;
    font-size: 14px;
    font-weight: 700;
    color: var(--ink);
    white-space: nowrap;
  }
  .spine .spine-imprint {
    position: absolute;
    bottom: 20px;
    left: 50%;
    transform: translateX(-50%);
    writing-mode: vertical-rl;
    display: flex;
    align-items: center;
    gap: 6px;
    font-size: 11px;
    font-weight: 700;
    color: var(--blue);
    white-space: nowrap;
  }
  .dot {
    display: inline-block;
    width: 12px;
    height: 12px;
    border-radius: 50%;
    background: var(--blue);
  }

  /* Back cover */
  .back .band-top { height: 32px; }
  .back .series {
    position: absolute;
    top: 74px; left: 0; right: 0;
    margin: 0;
    text-align: center;
    font-size: 20px;
    font-weight: 500;
  }
  .back .subtitle {
    position: absolute;
    top: 106px; left: 0; right: 0;
    margin: 0;
    text-align: center;
    font-size: 16px;
    font-weight: 700;
    color: var(--ink);
  }
  .back .rule-top { top: 146px; left: 60px; width: 240px; height: 1px; }
  .back .endorsement {
    position: absolute;
    top: 162px; left: 70px; right: 70px;
    margin: 0;
    text-align: center;
    font-size: 10px;
    font-style: italic;
    line-height: 14px;
    color: var(--ink);
  }
  .back .blurb {
    position: absolute;
    top: 236px; left: 38px; right: 38px;
    margin: 0;
    text-align: center;
    font-size: 9px;
    line-height: 14px;
    color: var(--ink);
  }
  .back .band-contact {
    position: absolute;
    left: 0; right: 0; top: 392px;
    height: 86px;
    background: var(--blue);
    padding: 24px 0 0 60px;
    box-sizing: border-box;
  }
  .back .band-contact p {
    margin: 0 0 10px;
    font-size: 9px;
    color: var(--white);
  }
  .back .imprint {
    position: absolute;
    top: 498px; left: 0; right: 0;
    display: flex;
    align-items: center;
    justify-content: center;
    gap: 8px;
    font-size: 17px;
    font-weight: 600;
    color: var(--blue);
  }
  .back .imprint .dot { width: 18px; height: 18px; }
</style>
</head>
<body>
<main class="canvas">
  <div class="book-wrap">

    <section class="cover back" aria-label="Back cover">
      <div class="band-top"></div>
      <h2 class="series"><span class="series-lead">Harbor</span> <span class="series-tail">Compass</span></h2>
      <p class="subtitle">Turning The Tide One Step at a Time</p>
      <div class="rule rule-top"></div>
      <p class="endorsement">"Positive endorsement or enticing description about your book goes here. The wording should be no more than three lines."</p>
      <p class="blurb">"Lorem Ipsum is simply dummy text of the printing and typesetting industry. Lorem Ipsum has been the industry's standard dummy text ever since the 1500s, when an unknown printer took a galley of type and scrambled it to make a type specimen book. It has survived not only five centuries, but also the leap into electronic typesetting, remaining essentially unchanged. It was popularised in the 1960s with the release of Typeline sheets containing Lorem Ipsum passages, and more recently with desktop publishing software like Pagecraft Studio including versions of Lorem Ipsum."</p>
      <div class="band-contact">
        <p>Contact details</p>
        <p>post adress</p>
      </div>
      <div class="imprint"><span class="dot"></span>Harbor Compass</div>
    </section>

    <section class="spine" aria-label="Spine">
      <p class="spine-title">Turning The Tide One Step at a Time</p>
      <div class="spine-imprint"><span class="dot"></span>Harbor Compass</div>
    </section>

    <section class="cover front" aria-label="Front cover">
      <div class="band-top"></div>
      <h2 class="series"><span class="series-lead">Harbor</span> <span class="series-tail">Compass</span></h2>
      <div class="rule rule-top"></div>
      <h1 class="title">
        Turning<br>
        <span class="accent">The Tide</span><br>
        One Step at a<br>
        <span class="soft">Time</span>
      </h1>
      <div class="rule rule-bottom"></div>
      <div class="band-quote">
        <p>"A three line quote from the book, description of the subject or positive endorsement from a reviewer. Use ten to twelve point size typeface"</p>
      </div>
      <p class="author">Author Name Here</p>
    </section>

  </div>
</main>
</body>
</html>
```